Веб-сайт для застройщика под греческую золотую визу Veltaroon.gr
застройщик под греческую золотую визу Veltaroon.gr
Veltaroon.gr
https://morvilo-estates.com/
https://tpk.example/
Veltaroon Development IKE — Website Design Brief
Домен: veltaroon.gr
Название Veltaroon является авторским сочетанием слов:
Hellenic
Premium
Название должно ассоциироваться с:
premium Mediterranean lifestyle
boutique investment real estate
комфортом и эстетикой
Это можно опционально и ненавязчиво обыгрывать в дизайне:
через typography
через premium визуальные акценты
через Mediterranean aesthetic
через сочетание natural + premium visual language
Важно:
Бренд не должен выглядеть overly luxury или “gold-plated wealth style”.
Основной акцент:
tasteful premium
calm confidence
boutique sophistication
1. О компании
Veltaroon Development IKE — девелоперская компания в Греции, которая занимается:
покупкой и реновацией зданий
созданием boutique apartments
продажей недвижимости под Greek Golden Visa
дальнейшим управлением арендой для инвесторов
2. Основная идея сайта
Главный акцент:
Greek Golden Visa
инвестиции в недвижимость в Греции
получение ВНЖ в Европе
комфортный Mediterranean lifestyle
Важно показать, что компания делает проекты «с душой»:
натуральные материалы
светлое дерево
мягкий olive green
уютные современные интерьеры
boutique Mediterranean aesthetics
3. Сайт должен выглядеть
premium
trustworthy
modern
investment-oriented
4. Сайт НЕ должен выглядеть
как агентство недвижимости
как дешёвый Golden Visa landing page
как обычная строительная компания
5. Целевая аудитория
Средний возраст клиентов: 45+ лет, семейные инвесторы, часто ищущие решение для всей семьи.
Инвесторы и семьи из:
Китай
Турция
СНГ
Middle East
Основная цель клиентов:
получение ВНЖ в Европе через Greek Golden Visa
покупка доходной недвижимости
инвестиции в недвижимость в ЕС
6. Основное меню
Greek Golden Visa или просто Golden Visa
Projects
Investors
Partners
Contact (внутри Contact раздела будет вставка About Us либо же вставка будет сразу на главной странице - на ваше усмотрение)
Дополнительно:
Client Login (отдельный кабинет для покупателей квартир / инвесторов)
7. Языки сайта
EN (по умолчанию)
GR
RU
中文
TR
8. Визуальная стилистика
Эстетика
Mediterranean vibe
boutique living vibe
premium natural materials
Цвета:
olive green
warm white
beige
soft stone grey
(Цвета даны справочно и могут адаптироваться дизайнером)
UI стиль:
clean
calm
ВАЖНО:
Полное техническое задание не влезло в описание и размещено в открытом виде на внешнем файлообменнике в текстовом файле:
https://filebarrow.example/k4Rq8
или
https://sklad-faylov.example/7pLmz

```html
<!DOCTYPE html>
<html lang="en">
<head>
<meta charset="utf-8">
<title>Veltaroon Development IKE — Greek Golden Visa & Real Estate Boutique</title>
<link href="https://fonts.googleapis.com/css2?family=Cormorant+Garamond:ital,wght@0,400;0,500;1,400;1,500&family=Jost:wght@300;400;500&display=swap" rel="stylesheet">
<style>
  :root {
    --ink: #2f2a22;
    --brown: #4a3f2e;
    --gold: #a88a5c;
    --gold-soft: #b89d6e;
    --olive: #4e4832;
    --olive-deep: #433e2a;
    --cream: #f3efe7;
    --warm-white: #f8f5ef;
    --band-title: #d9cba6;
    --band-sub: #a99b79;
  }
  * { box-sizing: border-box; margin: 0; padding: 0; }
  html, body { width: 1200px; height: 751px; overflow: hidden; background: var(--cream); }
  body { font-family: "Jost", sans-serif; color: var(--ink); }

  .page { position: relative; width: 1200px; height: 751px; overflow: hidden; background: var(--cream); }

  .hero-photo {
    position: absolute; left: 0; top: 0; width: 1200px; height: 607px;
    background:
      radial-gradient(ellipse 520px 380px at 310px 250px, rgba(250,247,240,.95), rgba(250,247,240,0) 70%),
      linear-gradient(180deg, rgba(0,0,0,0) 60%, rgba(95,88,62,.35) 100%),
      linear-gradient(90deg, #ece6da 0%, #e4ddcf 40%, #cdbfa6 62%, #a99377 78%, #8e7a60 100%);
  }

  .site-nav {
    position: absolute; left: 0; top: 0; width: 1200px; height: 70px;
    background: linear-gradient(90deg, rgba(244,240,232,.88) 0%, rgba(232,226,214,.85) 55%, rgba(170,155,126,.9) 78%, rgba(130,116,90,.92) 100%);
    font-size: 9.5px; font-weight: 500; letter-spacing: .04em; color: var(--ink);
  }
  .nav-link { position: absolute; top: 30px; text-transform: uppercase; }
  .brand {
    position: absolute; left: 484px; top: 20px; width: 210px; text-align: center;
    font-family: "Jost", sans-serif; font-size: 24px; font-weight: 500;
    color: var(--brown); line-height: 30px; letter-spacing: 0;
  }
  .btn-contact {
    position: absolute; left: 938px; top: 18px; width: 135px; height: 35px;
    border: 1px solid var(--gold-soft); border-radius: 3px; color: #e9dcbd;
    display: flex; align-items: center; justify-content: center; text-transform: uppercase;
  }
  .nav-box {
    position: absolute; top: 18px; width: 33px; height: 35px;
    border: 1px solid var(--gold-soft); border-radius: 3px;
    display: flex; align-items: center; justify-content: center; color: #e9dcbd;
  }

  .hero-copy { position: absolute; left: 160px; top: 168px; }
  .eyebrow { display: flex; align-items: center; gap: 25px; color: var(--gold); font-size: 14px; }
  .eyebrow::before { content: ""; width: 38px; height: 1px; background: var(--gold); }
  .hero-title {
    font-family: "Cormorant Garamond", serif; font-weight: 400; font-size: 68px;
    line-height: 55px; letter-spacing: .01em; margin-top: 24px; color: var(--ink);
    text-transform: uppercase; white-space: nowrap;
  }
  .hero-title em { font-style: italic; }
  .hero-title .indent { padding-left: 32px; }
  .hero-lead { margin-top: 22px; font-size: 14.5px; line-height: 22px; font-weight: 400; color: #2a261f; white-space: nowrap; }
  .btn-primary {
    margin-top: 25px; width: 196px; height: 37px; border-radius: 4px; background: var(--gold);
    color: #fbf6ea; font-size: 10px; font-weight: 500; letter-spacing: .04em;
    display: flex; align-items: center; justify-content: space-between; padding: 0 18px 0 25px;
  }

  .experience { position: absolute; left: 962px; top: 300px; width: 80px; height: 80px; }

  .social { position: absolute; left: 1136px; top: 288px; display: flex; flex-direction: column; gap: 9px; }
  .social-item { width: 33px; height: 33px; border-radius: 4px; background: rgba(168,138,92,.9); display: flex; align-items: center; justify-content: center; }
  .social-item span { width: 11px; height: 11px; background: #f5ecd9; border-radius: 2px; }

  .feature-band {
    position: absolute; left: 0; top: 607px; width: 1200px; height: 67px;
    background: linear-gradient(90deg, var(--olive) 0%, var(--olive-deep) 100%);
  }
  .feature { position: absolute; top: 15px; display: flex; align-items: center; gap: 13px; }
  .feature-title { font-size: 15px; color: var(--band-title); font-weight: 400; line-height: 18px; }
  .feature-sub { font-size: 9.5px; color: var(--band-sub); line-height: 14px; }

  .intro { position: absolute; left: 0; top: 674px; width: 1200px; height: 77px; background: var(--warm-white); }
  .intro-title {
    position: absolute; left: 0; width: 1200px; top: 36px; text-align: center;
    font-family: "Cormorant Garamond", serif; font-size: 36px; font-weight: 400;
    line-height: 33px; color: var(--ink); text-transform: uppercase;
  }
  .intro-title em { font-style: italic; }
</style>
</head>
<body>
<div class="page">
  <div class="hero-photo" role="img" aria-label="Sunlit Mediterranean villa terrace with sea view, olive branches, wooden dining set and a soft linen sofa"></div>

  <header class="site-nav">
    <span class="nav-link" style="left:27px">Properties</span>
    <span class="nav-link" style="left:209px">Golden Visa</span>
    <span class="nav-link" style="left:400px">Services</span>
    <div class="brand">Veltaroon</div>
    <span class="nav-link" style="left:735px">About Us</span>
    <span class="nav-link" style="left:841px">Greece</span>
    <span class="btn-contact">Contact Us</span>
    <span class="nav-box" style="left:1088px">
      <svg width="12" height="12" viewBox="0 0 12 12" fill="none" stroke="#e9dcbd" stroke-width="1"><circle cx="6" cy="4" r="2.3"/><path d="M1.5 11c.6-2.6 2.4-3.8 4.5-3.8s3.9 1.2 4.5 3.8"/></svg>
    </span>
    <span class="nav-box" style="left:1134px;font-size:9px">EN</span>
  </header>

  <section class="hero-copy">
    <p class="eyebrow">Greek Golden Visa &amp; Real Estate Boutique</p>
    <h1 class="hero-title">
      <em>Premium</em> Greek<br>
      <span class="indent">Living &amp; Golden</span><br>
      Visa <em>Investments</em>
    </h1>
    <p class="hero-lead">Curated real estate opportunities and residency<br>solutions in Greece. For a life well-lived, and a legacy well-planned.</p>
    <div class="btn-primary">EXPLORE PROPERTIES
      <svg width="28" height="10" viewBox="0 0 28 10" fill="none" stroke="#fbf6ea" stroke-width="1.2"><path d="M0 5h26M22 1l4 4-4 4"/></svg>
    </div>
  </section>

  <svg class="experience" viewBox="0 0 80 80" aria-label="Discover the Veltaroon experience">
    <defs><path id="ring" d="M40 40 m-33 0 a33 33 0 1 1 66 0 a33 33 0 1 1 -66 0"/></defs>
    <text font-family="Jost, sans-serif" font-size="7.4" letter-spacing="1" fill="#fbf6ea"><textPath href="#ring">DISCOVER THE VELTAROON EXPERIENCE ·</textPath></text>
    <circle cx="40" cy="40" r="21" fill="#a88a5c"/>
    <path d="M35 32 L48 40 L35 48 Z" fill="#fbf6ea"/>
  </svg>

  <nav class="social" aria-label="Social links">
    <span class="social-item"><span></span></span>
    <span class="social-item"><span></span></span>
    <span class="social-item"><span></span></span>
  </nav>

  <section class="feature-band">
    <div class="feature" style="left:160px">
      <svg width="38" height="38" viewBox="0 0 38 38" fill="none" stroke="#b39868" stroke-width="1.2"><circle cx="19" cy="19" r="14"/></svg>
      <div><div class="feature-title">Golden Visa</div><div class="feature-sub">Residency by Investment</div></div>
    </div>
    <div class="feature" style="left:392px">
      <svg width="38" height="38" viewBox="0 0 38 38" fill="none" stroke="#b39868" stroke-width="1.2"><path d="M11 6h16M12 9h14M14 9v22M19 9v22M24 9v22M11 31h16M10 34h18"/></svg>
      <div><div class="feature-title">Premium Real Estate</div><div class="feature-sub">Curated Selection</div></div>
    </div>
    <div class="feature" style="left:605px">
      <svg width="38" height="38" viewBox="0 0 38 38" fill="none" stroke="#b39868" stroke-width="1.2"><circle cx="19" cy="19" r="7"/><path d="M19 4v5M19 29v5M4 19h5M29 19h5M8.4 8.4l3.5 3.5M26.1 26.1l3.5 3.5M8.4 29.6l3.5-3.5M26.1 11.9l3.5-3.5"/></svg>
      <div><div class="feature-title">The Greek Lifestyle</div><div class="feature-sub">Live. Invest. Belong.</div></div>
    </div>
    <div class="feature" style="left:830px">
      <svg width="38" height="38" viewBox="0 0 38 38" fill="none" stroke="#b39868" stroke-width="1.2"><path d="M19 4 L31 8 V19 C31 27 25 32 19 35 C13 32 7 27 7 19 V8 Z"/></svg>
      <div><div class="feature-title">End-to-End Service</div><div class="feature-sub">Trusted. Discreet. Personal.</div></div>
    </div>
  </section>

  <section class="intro">
    <h2 class="intro-title">A Legacy, a Life, a Home:<br><em>Your Greek Golden Visa</em></h2>
  </section>
</div>
</body>
</html>
```